Need a mag/newspaper ad for an eyeweas sale

I attached an ad I used last year. Most of the infomation is similar but I want a totally DIFFERENT look.
Updates

Sorry but none of the ads submitted look like a high end retailer. They look like a chain ad, perhaps Glintmoor etc. Although this is a strong sale and discount, the fashion aspect must be shown in a clever and well thought out way.

Delvan I need to send you my modifications in a word document don't see where to do that so I need your email please. Thanks,Thomas

Target Market(s)

30 and older

Requirements
Must have
• Most of the information in the sample I attached but with a totally new exvciting look!
Nice to have
• Eyeglass graphics in the background and the use of exciting colors. We sell hiogh fashion and want to ad to look like an exciting place to shop.
Should not have
• ?

```html
<!DOCTYPE html>
<html lang="en">
<head>
<meta charset="utf-8">
<title>Harlow Opticians – Liquidation Sale Ad</title>
<link href="https://fonts.googleapis.com/css2?family=Didact+Gothic&family=Share+Tech+Mono&family=Oswald:wght@500;600&family=Open+Sans:wght@400;600;700&family=Russo+One&family=Tinos&display=swap" rel="stylesheet">
<style>
  :root {
    --page: #ffffff;
    --frame-outer: #9ec3f2;
    --frame-white: #ffffff;
    --sky-light: #c6e2fb;
    --sky-mid: #8fb3ee;
    --sky-deep: #5f7fd8;
    --violet: #9a93e0;
    --navy: #0c1a8c;
    --accent-blue: #2f7fe6;
    --ink: #0b0b0b;
    --white: #ffffff;
    --logo-red: #ee1c1c;
    --card-fill: rgba(235, 243, 255, 0.5);
    --card-edge: rgba(255, 255, 255, 0.85);
    --tag-fill: rgba(226, 232, 250, 0.85);
    --tag-bar: #5a5a66;
  }
  html, body {
    margin: 0; padding: 0;
    width: 1200px; height: 1000px;
    overflow: hidden;
    background: var(--page);
  }
  .canvas { position: relative; width: 1200px; height: 1000px; }

  .ad {
    position: absolute; left: 315px; top: 47px;
    width: 570px; height: 905px;
    background: linear-gradient(160deg, var(--sky-light), var(--frame-outer) 50%, var(--sky-deep));
  }
  .ad-frame {
    position: absolute; left: 12px; top: 15px; right: 12px; bottom: 15px;
    border: 13px solid var(--frame-white);
    overflow: hidden;
  }
  .bokeh-field {
    position: absolute; inset: 0;
    background:
      radial-gradient(circle at 88% 18%, rgba(255,255,255,0.6), transparent 22%),
      radial-gradient(circle at 30% 48%, rgba(255,255,255,0.22) 0 11%, transparent 12%),
      radial-gradient(circle at 62% 58%, rgba(255,255,255,0.18) 0 9%, transparent 10%),
      radial-gradient(circle at 15% 78%, rgba(255,255,255,0.16) 0 12%, transparent 13%),
      radial-gradient(circle at 82% 74%, rgba(255,255,255,0.16) 0 10%, transparent 11%),
      radial-gradient(circle at 48% 88%, rgba(255,255,255,0.14) 0 8%, transparent 9%),
      radial-gradient(circle at 70% 82%, rgba(180,170,240,0.5), transparent 35%),
      linear-gradient(175deg, var(--sky-light) 0%, var(--sky-mid) 35%, #7f9de8 65%, var(--violet) 85%, var(--sky-deep) 100%);
  }
  .lens-graphic {
    position: absolute; left: 270px; top: 150px;
    width: 210px; height: 115px;
    border-radius: 50%;
    transform: rotate(-8deg);
    background: radial-gradient(ellipse at 40% 45%, rgba(255,255,255,0.45), rgba(200,215,250,0.25) 60%, transparent 72%);
  }

  .el { position: absolute; }

  .headline {
    left: 0; width: 100%; top: 18px; margin: 0;
    text-align: center;
    font-family: "Didact Gothic", sans-serif;
    font-weight: 400;
    font-size: 78px; line-height: 1; letter-spacing: 1px;
    color: var(--sky-light);
    -webkit-text-stroke: 1.3px var(--navy);
  }
  .subhead {
    left: 0; width: 100%; top: 98px; margin: 0;
    text-align: center;
    font-family: "Share Tech Mono", monospace;
    font-weight: 400;
    font-size: 40px; line-height: 1; letter-spacing: 1px;
    color: var(--navy);
  }

  .anniversary {
    left: 300px; top: 160px; width: 200px;
    text-align: center;
    font-family: "Open Sans", sans-serif;
    font-size: 36px; line-height: 1.05;
    color: var(--accent-blue);
    transform: rotate(-9deg);
  }
  .anniversary sup { font-size: 18px; }

  .offer-card {
    background: var(--card-fill);
    border: 2px solid var(--card-edge);
    text-align: center;
    color: var(--ink);
    font-family: "Oswald", sans-serif;
    font-weight: 600;
    box-sizing: border-box;
  }
  .offer-card .percent { font-size: 38px; line-height: 1.1; display: block; }
  .offer-card .item { font-size: 30px; line-height: 1.1; display: block; }
  .offer-card .extra { font-family: "Open Sans", sans-serif; font-weight: 400; font-size: 18px; display: block; line-height: 1.1; }
  .offer-card .fine { font-family: "Open Sans", sans-serif; font-weight: 400; font-size: 9.5px; display: block; line-height: 1.3; }

  .card-frames {
    left: 8px; top: 172px; width: 285px; height: 150px;
    transform: rotate(-14deg);
    padding-top: 10px;
  }
  .card-frames .percent { font-size: 37px; }
  .card-frames .item { font-size: 33px; }
  .card-sunglasses {
    left: 235px; top: 280px; width: 268px; height: 158px;
    transform: rotate(-3deg);
    padding-top: 12px;
  }
  .card-sunglasses .item { font-size: 28px; line-height: 1.12; }

  .price-tag {
    background: var(--tag-fill);
    border-top: 4px solid var(--tag-bar);
    border-radius: 0 0 48px 48px;
    text-align: center;
    font-family: "Open Sans", sans-serif;
    color: var(--ink);
    box-sizing: border-box;
  }
  .price-tag .lead { font-weight: 700; display: block; line-height: 1; }
  .price-tag .detail { font-size: 13px; display: block; line-height: 1.3; }
  .price-tag .amount { font-weight: 600; display: block; line-height: 1.1; }
  .price-tag .note { font-size: 11px; display: block; line-height: 1.2; }
  .tag-single { left: 110px; top: 337px; width: 98px; height: 165px; padding-top: 10px; }
  .tag-single .lead { font-size: 19px; }
  .tag-single .amount { font-size: 36px; }
  .tag-hd { left: 8px; top: 470px; width: 102px; height: 172px; padding-top: 10px; }
  .tag-hd .lead { font-size: 34px; }
  .tag-hd .detail { font-size: 11px; }
  .tag-hd .amount { font-size: 30px; margin-top: 4px; }

  .expiry {
    left: 200px; top: 458px; width: 330px;
    font-family: "Russo One", sans-serif;
    font-size: 20px; letter-spacing: 1.5px;
    color: var(--white); text-align: center;
  }
  .logo-slot {
    left: 175px; top: 522px; width: 340px;
    font-family: "Russo One", sans-serif;
    font-size: 46px; letter-spacing: 2px;
    color: var(--logo-red); text-align: center;
  }

  .store-info {
    left: 0; width: 100%; top: 646px;
    text-align: center; color: var(--white);
    font-family: "Open Sans", sans-serif;
  }
  .store-info .location { font-weight: 700; font-size: 15.5px; margin: 0; }
  .store-info .landmarks { font-size: 10.5px; margin: 2px 0 0; font-weight: 600; }
  .store-info .phone { font-weight: 700; font-size: 46px; margin: 4px 0 0; line-height: 1.15; }
  .store-info .hours { font-weight: 700; font-size: 16px; margin: 0; }
  .store-info .web { font-weight: 700; font-size: 18px; margin: 7px 0 0; }
  .tagline {
    left: 0; width: 100%; top: 790px;
    text-align: center; margin: 0;
    font-family: "Tinos", serif;
    font-size: 36px; color: var(--white);
  }
</style>
</head>
<body>
<div class="canvas">
  <div class="ad">
    <div class="ad-frame">
      <div class="bokeh-field" role="img" aria-label="Soft blue and violet bokeh light background"></div>
      <div class="lens-graphic" role="img" aria-label="Faint designer eyeglass lens graphic"></div>

      <h1 class="el headline">LIQUIDATION</h1>
      <h2 class="el subhead">OF DESIGNER FRAMES!</h2>

      <div class="el anniversary">OUR 30<sup>TH</sup><br>YEAR !</div>

      <div class="el offer-card card-frames">
        <span class="percent">40% - 75%</span>
        <span class="item">OFF Rx FRAMES</span>
        <span class="extra">PLUS $100 OFF LENSES</span>
        <span class="fine">Lens purchase necessary. Certain names excluded.</span>
      </div>

      <div class="el offer-card card-sunglasses">
        <span class="percent">40% - 75%</span>
        <span class="item">OFF NON<br>RX SUNGLASSES</span>
        <span class="fine" style="margin-top:6px">Grab 'n Go or put your RX in them to save more !<br>Certain Names Excluded.</span>
      </div>

      <div class="el price-tag tag-single">
        <span class="lead">SINGLE</span>
        <span class="detail">VISION<br>LENSES<br>FROM</span>
        <span class="amount">$50</span>
        <span class="note">After<br>Discount</span>
      </div>

      <div class="el price-tag tag-hd">
        <span class="lead">HD</span>
        <span class="detail">PROGRESSIVE<br>LENSES FROM</span>
        <span class="amount">$220</span>
        <span class="note">After<br>Discount</span>
      </div>

      <div class="el expiry">OFFER EXPIRES 09-30-14</div>
      <div class="el logo-slot">YOUR LOGO</div>

      <div class="el store-info">
        <p class="location">SHOPS AT LINDEN CENTER ON MAPLE TRAIL</p>
        <p class="landmarks">(Next to Marco's Tacos Restaurant and Auntie Lin's Restaurant)</p>
        <p class="phone">561-555-0148</p>
        <p class="hours">Open Mon. - Wed. 10-6&nbsp; Thurs. - Sat. 10-9</p>
        <p class="web">HarlowOpticians.com</p>
      </div>
      <p class="el tagline">We Only Sell What We Love!</p>
    </div>
  </div>
</div>
</body>
</html>
```